Website Design and Build

This is a design and build of a dating site.

100% the most important thing is for the website to look good. I want this thing to be stunning and feel like a premium product so please only tender for the job if you excel at design and use of colours.

Theme is: premium, professional & uncluttered
Colour Scheme is: bright, fun and friendly but also reassuring and professional
 
Platforms: Initially just browser based (desktop and mobile) but if the proof of concept works we will roll it out to apps across the major platforms.

Marketing will be done primarily through organic online searches and content driven leads to a squeeze page, so SEO optimisation and experience with squeeze pages also a must.

Please include examples of sites you’ve done or other sites you think give a flavour of your vision for what this site will be. Any thoughts on palettes/colour scheme also useful.

I will provide the full brief to the successful designer.

Thank you for your time.

Industry/Entity Type

Dating

Coding

Coded - Design and coding required

Number of Pages Required

5+ page

Font styles to use
Sans Serif

Colors

Designer to choose colors to be used in the design.

Requirements
Must have
• Professional, Premium and uncluttered look.
• SEO optimisation.
• Squeeze page.
• A way to track different lead sources e.g. some of it will be content led to a squeeze page, some of it organic search engine hits, some of it unique referral links given to specific bloggers/influencers. I want to be able to track the success of all the different types of generating traffic to the site.
• I also want to be able to amend/update the site myself going forward so would like the spec/design to be clearly documented to allow me to do this.

```html
<!DOCTYPE html>
<html lang="en">
<head>
<meta charset="utf-8">
<title>Evergreen Hearts — Dating</title>
<link href="https://fonts.googleapis.com/css2?family=Open+Sans:wght@300;400;600;700&display=swap" rel="stylesheet">
<style>
:root{
  --purple:#8d3cae;
  --purple-dark:#7a2f9a;
  --purple-soft:#a45bc2;
  --yellow:#fbbd18;
  --yellow-light:#fdd233;
  --orange:#f6a70f;
  --white:#ffffff;
  --ink:#3b3b3b;
  --grey-text:#8a8a8a;
  --grey-bg:#f3f3f3;
  --phone:#2c2c30;
}
*{box-sizing:border-box;margin:0;padding:0}
html,body{width:1200px;height:900px;overflow:hidden}
body{font-family:"Open Sans",Arial,sans-serif;background:var(--white);position:relative;color:var(--ink)}
.btn{position:absolute;background:var(--yellow);color:var(--ink);font-weight:600;text-transform:uppercase;border-radius:20px;display:flex;align-items:center;justify-content:center;letter-spacing:.3px;white-space:nowrap}

/* left column */
.mobile-page{position:absolute;left:0;top:0;width:447px;height:900px;overflow:hidden}
.hero{position:absolute;left:0;top:0;width:447px;height:258px;background:var(--purple);overflow:hidden}
.hero-photo{position:absolute;left:0;top:0;width:222px;height:258px;background:linear-gradient(135deg,#b98fb8 0%,#8b6a86 45%,#6d4e73 100%)}
.hero-photo-arc{position:absolute;left:-30px;top:192px;width:150px;height:150px;border-radius:50%;background:var(--white)}
.brand-circle{position:absolute;left:284px;top:18px;width:74px;height:74px;border-radius:50%;background:var(--white);display:flex;align-items:center;justify-content:center;text-align:center;color:var(--purple);font-size:9px;font-weight:600;line-height:1.2;text-transform:uppercase}
.hero-tagline{position:absolute;left:222px;width:225px;top:110px;text-align:center;color:var(--white);font-size:12px;line-height:1;font-weight:300;text-transform:uppercase}
.hero-title{position:absolute;left:222px;width:225px;top:124px;text-align:center;color:var(--white);font-size:22px;line-height:1;font-weight:700;text-transform:uppercase}
.field{position:absolute;height:17px;background:var(--white);border-radius:10px;font-size:6.5px;color:var(--grey-text);display:flex;align-items:center;padding:0 8px;justify-content:space-between;white-space:nowrap}
.field::after{content:"";border:3px solid transparent;border-top-color:var(--ink);margin-top:3px;margin-left:4px}
.field.plain::after{display:none}
.small-note{position:absolute;left:222px;width:225px;text-align:center;font-size:6px;color:var(--white)}

.about{position:absolute;left:0;top:258px;width:447px;height:135px;background:var(--white);text-align:center}
.section-title{font-size:11px;text-transform:uppercase;color:var(--ink);font-weight:400;letter-spacing:.3px}
.about .section-title{margin-top:40px}
.about p{width:320px;margin:10px auto 0;font-size:6.5px;line-height:1.55;color:var(--grey-text)}

.features{position:absolute;left:0;top:393px;width:447px;height:201px;background:var(--purple)}
.features .section-title{position:absolute;top:38px;width:100%;text-align:center;color:var(--yellow)}
.feature{position:absolute;top:75px;width:84px;text-align:center;color:var(--white)}
.feature svg{display:block;margin:0 auto;width:32px;height:32px}
.feature h4{margin-top:14px;font-size:7px;font-weight:600;color:var(--yellow);text-transform:uppercase}
.feature p{margin-top:3px;font-size:5.5px;line-height:1.4;font-weight:300}

.app{position:absolute;left:0;top:594px;width:447px;height:306px;background:var(--white)}
.app .section-title{position:absolute;top:38px;width:100%;text-align:center}
.app-ring{position:absolute;left:155px;top:110px;width:140px;height:140px;border-radius:50%;border:5px solid var(--purple)}
.side-bubble{position:absolute;top:123px;width:68px;height:68px;border-radius:50%;border:1px solid #e6e6e6;font-size:6.5px;color:var(--grey-text);display:flex;align-items:center;justify-content:center;text-align:center;padding:10px;line-height:1.4}
.phone{position:absolute;left:180px;top:66px;width:90px;height:180px;background:var(--phone);border-radius:12px}
.phone-screen{position:absolute;left:4px;top:16px;width:82px;height:148px;background:var(--white);overflow:hidden}
.phone-url{background:#eee;font-size:4.5px;color:var(--grey-text);text-align:center;padding:2px 0}
.phone-brand{font-size:6.5px;color:var(--purple);text-transform:uppercase;text-align:center;padding:4px 0;font-weight:600}
.phone-card{margin:0 8px;height:100px;background:var(--purple);padding:5px}
.phone-photo{height:62px;background:linear-gradient(160deg,#c99a7b,#8c5b48)}
.phone-name{font-size:5px;color:var(--white);margin-top:3px}
.phone-actions{display:flex;justify-content:center;gap:8px;margin-top:6px}
.phone-actions span{width:12px;height:8px;background:var(--white);border-radius:4px}
.phone-home{position:absolute;left:39px;bottom:5px;width:12px;height:12px;border-radius:50%;border:1px solid #555}

/* right page */
.online{position:absolute;left:447px;top:0;width:753px;height:366px;background:radial-gradient(circle at 50% 30%,var(--yellow-light) 0%,var(--yellow) 55%,var(--orange) 100%)}
.online h2{position:absolute;top:84px;width:100%;text-align:center;color:var(--purple);font-weight:400;font-size:20px;text-transform:uppercase}
.avatar{position:absolute;border-radius:50%;border:4px solid var(--white);box-shadow:0 3px 8px rgba(0,0,0,.15)}
.intro{position:absolute;left:447px;top:366px;width:753px;height:450px;background:var(--grey-bg);overflow:hidden}
.intro-photo{position:absolute;left:0;top:0;width:430px;height:450px;background:linear-gradient(100deg,#e2ddd9 0%,#bfa394 40%,#d5b7a6 70%,#ece8e6 100%)}
.intro-ring{position:absolute;left:0;top:0}
.intro-kicker{position:absolute;left:471px;top:130px;font-size:14px;line-height:1;color:var(--grey-text);text-transform:uppercase}
.intro-title{position:absolute;left:471px;top:152px;font-size:29px;line-height:42px;color:var(--purple);font-weight:300;text-transform:uppercase;white-space:nowrap}
.footer{position:absolute;left:447px;top:816px;width:753px;height:84px;background:var(--purple);color:var(--white);display:flex;align-items:center}
.protected{margin-left:22px;font-size:11px;text-transform:uppercase;display:flex;align-items:center;gap:10px}
.badge{width:60px;height:26px;border-radius:4px;background:var(--purple-soft)}
.footer-nav{margin-left:auto;display:flex;gap:20px;font-size:13px;margin-right:22px}
.footer-nav a{color:var(--white);text-decoration:none}
.footer-nav .accent{color:var(--yellow)}
.to-top{width:22px;height:22px;border-radius:50%;background:var(--white);margin-right:16px;display:flex;align-items:center;justify-content:center}
</style>
</head>
<body>

<section class="mobile-page">
  <header class="hero">
    <div class="hero-photo" role="img" aria-label="Photo of a smiling couple embracing"></div>
    <div class="hero-photo-arc"></div>
    <div class="brand-circle">Evergreen<br>Hearts</div>
    <p class="hero-tagline">It is never too late to</p>
    <h1 class="hero-title">Fall in love</h1>
    <div class="field" style="left:251px;top:152px;width:76px">I am a man</div>
    <div class="field" style="left:331px;top:152px;width:71px">Seeking a woman</div>
    <div class="field plain" style="left:251px;top:176px;width:151px">First name</div>
    <div class="btn" style="left:251px;top:200px;width:151px;height:17px;font-size:7.5px">Sign up for free</div>
    <p class="small-note" style="top:225px">Already have an account? Log in</p>
  </header>

  <section class="about">
    <h2 class="section-title">Never ending romance</h2>
    <p>Finding someone special should feel simple and safe. Our members are real people looking for genuine connection, and every profile is reviewed by our team. Take your time, share what matters to you and meet people who value the same things.</p>
  </section>

  <section class="features">
    <h2 class="section-title">Why you'll love Evergreen Hearts</h2>
    <div class="feature" style="left:36px">
      <svg viewBox="0 0 32 32" fill="none" stroke="#fff" stroke-width="1.5"><path d="M16 3 L27 7 V15 C27 22 22 27 16 29 C10 27 5 22 5 15 V7 Z"/><path d="M16 3 V29"/></svg>
      <h4>Protection</h4><p>Your data is guarded by leading encryption.</p>
    </div>
    <div class="feature" style="left:132px">
      <svg viewBox="0 0 32 32" fill="none" stroke="#fff" stroke-width="1.5"><rect x="5" y="5" width="22" height="22" rx="6"/><path d="M10 16 L14.5 20.5 L22 12"/></svg>
      <h4>Verification</h4><p>Every member is personally confirmed by our staff.</p>
    </div>
    <div class="feature" style="left:228px">
      <svg viewBox="0 0 32 32" fill="none" stroke="#fff" stroke-width="1.5"><circle cx="13" cy="13" r="8"/><path d="M19 19 L28 28"/></svg>
      <h4>Attention</h4><p>Thoughtful matches chosen around your interests.</p>
    </div>
    <div class="feature" style="left:324px">
      <svg viewBox="0 0 32 32" fill="none" stroke="#fff" stroke-width="1.5"><circle cx="12" cy="11" r="5"/><path d="M3 26 C3 19 21 19 21 26"/><circle cx="21" cy="11" r="5"/><path d="M20 19 C25 19 29 21 29 26"/></svg>
      <h4>Communication</h4><p>Chat, video calls and private messages.</p>
    </div>
  </section>

  <section class="app">
    <h2 class="section-title">All in one place and on the go</h2>
    <div class="app-ring"></div>
    <div class="side-bubble" style="left:66px">Discover people near you</div>
    <div class="side-bubble" style="left:313px">Matches by interests</div>
    <div class="phone">
      <div class="phone-screen">
        <div class="phone-url">evergreenhearts.com</div>
        <div class="phone-brand">Evergreen Hearts</div>
        <div class="phone-card">
          <div class="phone-photo" role="img" aria-label="Member profile photo"></div>
          <div class="phone-name">Nadia</div>
          <div class="phone-actions"><span></span><span></span></div>
        </div>
      </div>
      <div class="phone-home"></div>
    </div>
    <div class="btn" style="left:162px;top:262px;width:120px;height:16px;font-size:7px">Join now and explore</div>
  </section>
</section>

<section class="online">
  <h2>There are many people online right now</h2>
  <div class="avatar" role="img" aria-label="Member portrait" style="left:33px;top:159px;width:96px;height:96px;background:linear-gradient(160deg,#e9d2c3,#b58f78)"></div>
  <div class="avatar" role="img" aria-label="Member portrait" style="left:236px;top:165px;width:74px;height:74px;background:linear-gradient(160deg,#cfb39e,#6e5646)"></div>
  <div class="avatar" role="img" aria-label="Member portrait" style="left:420px;top:153px;width:96px;height:96px;background:linear-gradient(160deg,#d99170,#9b4a2f)"></div>
  <div class="avatar" role="img" aria-label="Member portrait" style="left:626px;top:165px;width:74px;height:74px;background:linear-gradient(160deg,#c9ad98,#5f4637)"></div>
</section>

<section class="intro">
  <div class="intro-photo" role="img" aria-label="Photo of a happy couple hugging"></div>
  <svg class="intro-ring" width="430" height="450" viewBox="0 0 430 450" fill="none">
    <circle cx="212" cy="305" r="195" stroke="#8d3cae" stroke-width="6"/>
  </svg>
  <p class="intro-kicker">Evergreen Hearts</p>
  <h2 class="intro-title">Where true<br>love stands the<br>test of time</h2>
  <div class="btn" style="left:468px;top:300px;width:197px;height:33px;font-size:14px">Join free today</div>
</section>

<footer class="footer">
  <div class="protected">Protected by <span class="badge"></span></div>
  <nav class="footer-nav">
    <a href="#">About</a><a href="#">Terms</a><a href="#">Privacy</a><a href="#">Contact</a><a href="#">Login</a><a href="#" class="accent">Sign Up</a>
  </nav>
  <div class="to-top"><svg width="10" height="8" viewBox="0 0 10 8"><path d="M5 1 L9 7 H1 Z" fill="#3b3b3b"/></svg></div>
</footer>

</body>
</html>
```